Re-branding for Structural Engineering firm

We need new business cards as part of our current re-branding. We have a new logo (attached), so the card design should incorporate this color scheme. We are a structural engineering firm providing structural building design and seismic consulting services. The final design should communicate professionalism and stability, with a modern look and feel.

```html
<!DOCTYPE html>
<html lang="en">
<head>
<meta charset="utf-8">
<title>RMV Structural Engineering – Business Card</title>
<link href="https://fonts.googleapis.com/css2?family=Lato:wght@400;700&display=swap" rel="stylesheet">
<style>
  :root {
    --page-bg: #e6e4e1;
    --card-black: #0b0c0e;
    --card-navy: #0e1c2b;
    --brand-blue: #1f84c9;
    --brand-gray: #a6a7a9;
    --text-light: #e9e9ea;
    --text-soft: #c9cacc;
  }
  html, body {
    margin: 0;
    width: 1200px;
    height: 1200px;
    overflow: hidden;
    background: var(--page-bg);
    font-family: "Lato", sans-serif;
  }
  .card {
    position: absolute;
    left: 75px;
    top: 300px;
    width: 1050px;
    height: 600px;
    background: var(--card-black);
    overflow: hidden;
    box-shadow: 0 14px 40px rgba(0,0,0,0.25);
  }
  .card-shapes {
    position: absolute;
    inset: 0;
  }
  .brand {
    position: absolute;
    left: 790px;
    top: 70px;
    color: var(--brand-gray);
    font-weight: 700;
    line-height: 1;
  }
  .brand-square {
    width: 150px;
    height: 150px;
    background: var(--brand-blue);
    margin-bottom: 26px;
  }
  .brand-name {
    font-size: 60px;
    letter-spacing: 4px;
  }
  .brand-sub {
    font-size: 25px;
    letter-spacing: 1px;
    margin-top: 10px;
    line-height: 1.15;
  }
  .person {
    position: absolute;
    left: 110px;
    top: 345px;
    color: var(--text-light);
  }
  .person-name {
    font-weight: 700;
    font-size: 40px;
    letter-spacing: -0.5px;
    margin: 0;
  }
  .person-title {
    font-size: 27px;
    color: var(--text-soft);
    margin: 4px 0 0 10px;
  }
  .contact {
    position: absolute;
    top: 438px;
    font-size: 25px;
    line-height: 33px;
    color: var(--text-light);
    letter-spacing: -0.3px;
  }
  .contact-direct { left: 120px; }
  .contact-address { left: 370px; }
  .contact p { margin: 0; }
</style>
</head>
<body>
  <div class="card">
    <svg class="card-shapes" width="1050" height="600" viewBox="0 0 1050 600" aria-hidden="true">
      <polygon class="navy-panel" points="0,0 300,0 690,600 0,600" fill="var(--card-navy)"/>
      <rect class="band-blue" x="0" y="548" width="680" height="52" fill="var(--brand-blue)"/>
      <polygon class="band-gray" points="630,515 1050,515 1050,600 690,600" fill="var(--brand-gray)"/>
    </svg>

    <div class="brand">
      <div class="brand-square"></div>
      <div class="brand-name">RMV</div>
      <div class="brand-sub">STRUCTURAL<br>ENGINEERING</div>
    </div>

    <div class="person">
      <h1 class="person-name">JOHN DOE</h1>
      <p class="person-title">Director</p>
    </div>

    <div class="contact contact-direct">
      <p>858.555.0142</p>
      <p>jdoe@rmvse.com</p>
      <p>www.rmvse.com</p>
    </div>

    <div class="contact contact-address">
      <p>4150 Alder Ridge Rd.</p>
      <p>Ste.210, San Diego, California 92121</p>
    </div>
  </div>
</body>
</html>
```